Wheatless Table Co Web Design

We are looking for designs for a homepage for a gluten free, health food website.

We are looking for the site to be a shop, as well as a resource/information source for users. We will also look to incorporate recipes, blogs, forums and potentially some other useful information.

We want to ensure that the website is user-friendly, does not have a corporate feel, but is still classy.

We want to have high quality photographic images in the background, with text in the foreground - but these things will need to compliment each other well. e.g recipe of the week integrated onto the background photo and the 'shop' in the foreground.

We have seen a site that we quite like and although we like the design, we do not want to completely emulate this. However, it is a useful starting point for designers and perhaps some inspiration www.brambleharvestgrocer.example

We already have a logo - see attached - which will need to be fully integrated into the design.

We do want a colourful design, but mainly in terms of the images rather than the graphics.
Updates

Please note:

We are pleased with the designs to date, for the most part. We would like you all to note, however, that we are much preferring the lighter designs - ones that make the sites feel brighter - rather than those which are darker in appearance.

We would also like to see less space allocated to the main image, within the context of the site as a whole.

Thanks.

We have eliminated those which we feel are not what we are looking for. We are still keen to see some more designs and are still looking for something unique. There are some good things in all of the designs that we have not eliminated, however we still feel there is room for more inspiration.

Thanks.

Target Market(s)

Our audience are body conscience people looking for health food products. They are also those who are potentially looking for a new lifestyle/life cha

Industry/Entity Type

Health

Requirements
Must have
• Our logo - attached, can provide variations in due course.

Navigational features as per mock up attached.

Social network integration.

NB: we only need one (home) page for this.

```html
<!DOCTYPE html>
<html lang="en">
<head>
<meta charset="utf-8">
<title>Wheatless Table Co — Home</title>
<link href="https://fonts.googleapis.com/css2?family=Arimo:wght@400;700&family=Cinzel:wght@400;600;700&family=Mulish:wght@400;600;700&family=Fira+Sans:wght@400;500&family=Raleway:wght@400;500&display=swap" rel="stylesheet">
<style>
  :root {
    --ink: #111111;
    --bar: #1a1a1a;
    --panel: rgba(255,255,255,0.95);
    --orange: #f07c21;
    --orange-dark: #e0661a;
    --teal: #1f5c50;
    --rule: #cfcfcf;
    --white: #ffffff;
    --icon-bg: #f2f2f2;
  }
  * { box-sizing: border-box; margin: 0; padding: 0; }
  html, body { width: 1200px; height: 890px; overflow: hidden; background: #2a2320; }
  .page { position: relative; width: 1200px; height: 890px; overflow: hidden; font-family: "Mulish", sans-serif; }

  /* top bar */
  .topbar { position: absolute; left: 0; top: 0; width: 1200px; height: 46px; background: var(--bar); }
  .topnav { position: absolute; left: 628px; top: 0; height: 46px; display: flex; align-items: center; font-family: "Arimo", sans-serif; font-size: 16px; color: var(--white); }
  .topnav a { color: var(--white); text-decoration: none; padding: 0 18px; border-left: 1px solid #444; line-height: 18px; }
  .topnav a:first-child { border-left: none; }
  .search { position: absolute; left: 934px; top: 10px; width: 226px; height: 26px; background: #050505; border: 1px solid #3a3a3a; font-family: "Arimo", sans-serif; font-size: 14px; color: #9a9a9a; padding: 4px 8px; }
  .search svg { position: absolute; right: 7px; top: 4px; }

  /* background scene */
  .backdrop { position: absolute; left: 0; top: 46px; width: 1200px; height: 743px;
    background:
      radial-gradient(ellipse 30% 18% at 72% 96%, #6b3e22 0%, rgba(107,62,34,0) 100%),
      radial-gradient(ellipse 40% 20% at 96% 5%, #3a2820 0%, rgba(58,40,32,0) 100%),
      radial-gradient(ellipse 60% 45% at 45% 55%, #eeeae6 0%, rgba(238,234,230,0) 100%),
      linear-gradient(180deg, #8a7468 0%, #cfc6bf 30%, #dcd6d1 60%, #9a7c68 100%); }

  /* sidebar */
  .sidebar { position: absolute; left: 22px; top: 46px; width: 237px; height: 713px; background: var(--panel); }
  .brand { position: absolute; left: 0; top: 108px; width: 237px; display: flex; align-items: center; justify-content: center; gap: 8px; font-family: "Cinzel", serif; font-weight: 700; font-size: 17px; color: var(--ink); }
  .brand-dot { width: 16px; height: 16px; border-radius: 50%; background: var(--ink); flex: none; }
  .mainnav { position: absolute; left: 7px; top: 179px; width: 220px; list-style: none; }
  .mainnav li { height: 43.4px; border-bottom: 1px dashed var(--rule); font-family: "Cinzel", serif; font-size: 17px; text-transform: uppercase; letter-spacing: 1.5px; color: var(--ink); padding-left: 24px; line-height: 43px; }
  .mainnav li:last-child { border-bottom: none; }
  .mainnav li.active { color: var(--white); background: var(--ink); margin-left: 5px; padding-left: 19px; position: relative; width: 230px; }
  .mainnav li.active::before { content: ""; position: absolute; left: -13px; top: 0; border-top: 21.7px solid transparent; border-bottom: 21.7px solid transparent; border-right: 13px solid var(--ink); }
  .submenu { position: absolute; left: 259px; top: 399px; width: 166px; height: 144px; background: #1b1b1b; list-style: none; padding: 7px 6px 0 6px; }
  .submenu li { height: 31.5px; line-height: 31px; border-bottom: 1px dashed #444; font-family: "Cinzel", serif; font-size: 14px; font-weight: 600; text-transform: uppercase; color: var(--white); padding-left: 15px; letter-spacing: 0.5px; }
  .submenu li:last-child { border-bottom: none; }

  /* hero */
  .hero { position: absolute; left: 294px; top: 78px; width: 862px; height: 302px; background: var(--white); border: 2px solid var(--white); box-shadow: 0 1px 4px rgba(0,0,0,0.35); }
  .hero-intro { position: absolute; left: 0; top: 0; width: 258px; height: 298px;
    background: linear-gradient(90deg, rgba(255,255,255,0.95) 0%, rgba(255,255,255,0.86) 100%), linear-gradient(180deg, #d9d1c6, #b99f86); }
  .hero-title { position: absolute; left: 24px; top: 40px; font-family: "Cinzel", serif; font-weight: 700; font-size: 23px; line-height: 28px; color: var(--ink); }
  .hero-text { position: absolute; left: 24px; top: 122px; width: 220px; font-size: 15px; line-height: 22px; color: var(--ink); }
  .btn-more { position: absolute; left: 24px; top: 215px; width: 161px; height: 32px; border-radius: 16px; background: linear-gradient(var(--orange), var(--orange-dark)); color: var(--white); font-weight: 700; font-size: 15px; line-height: 32px; padding-left: 16px; box-shadow: 0 2px 3px rgba(0,0,0,0.3); }
  .hero-photo { position: absolute; left: 258px; top: 0; width: 600px; height: 298px;
    background:
      radial-gradient(ellipse 14% 18% at 47% 60%, #c9433a 0%, rgba(201,67,58,0) 100%),
      radial-gradient(ellipse 22% 22% at 40% 45%, #e4a08c 0%, rgba(228,160,140,0) 100%),
      radial-gradient(ellipse 18% 20% at 22% 40%, #f0dc8a 0%, rgba(240,220,138,0) 100%),
      radial-gradient(ellipse 14% 22% at 72% 70%, #9bb04a 0%, rgba(155,176,74,0) 100%),
      radial-gradient(ellipse 16% 16% at 62% 28%, #6ca24a 0%, rgba(108,162,74,0) 100%),
      radial-gradient(ellipse 55% 48% at 55% 62%, #5a3a2a 0%, rgba(90,58,42,0) 100%),
      linear-gradient(180deg, #d8cfc2 0%, #efece6 55%, #e3ddd4 100%); }

  /* daily picks */
  .picks-bar { position: absolute; left: 455px; top: 416px; width: 696px; height: 48px; background: var(--white); border-radius: 24px; text-align: center; font-family: "Fira Sans", sans-serif; font-size: 35px; line-height: 46px; color: var(--teal); }
  .picks-arrow { position: absolute; top: 3px; width: 42px; height: 42px; }
  .picks-arrow.prev { left: 4px; }
  .picks-arrow.next { right: 4px; }

  .pick { position: absolute; top: 518px; width: 223px; height: 241px; border: 6px solid var(--orange); background: var(--orange); }
  .pick-tab { position: absolute; top: -47px; left: 50%; width: 106px; height: 54px; margin-left: -53px; background: var(--orange); border-radius: 53px 53px 0 0; color: var(--white); font-family: "Fira Sans", sans-serif; font-weight: 500; font-size: 20px; text-align: center; padding-top: 14px; letter-spacing: 0.5px; }
  .pick-body { position: absolute; inset: 0; background: var(--white); border: 1px solid var(--teal); }
  .pick-photo { width: 100%; height: 139px; }
  .pick-stars { margin: 5px 0 0 7px; font-size: 18px; line-height: 22px; color: var(--teal); font-family: "Arimo", sans-serif; letter-spacing: 0; }
  .pick-stars span { color: #222; font-family: "Fira Sans", sans-serif; font-size: 17px; margin-left: 5px; }
  .pick-name { margin: 2px 7px 0 7px; font-family: "Fira Sans", sans-serif; font-size: 16px; line-height: 22px; color: var(--teal); }

  /* footer */
  .footer { position: absolute; left: 0; top: 789px; width: 1200px; height: 101px; background: #000; font-family: "Raleway", sans-serif; color: var(--white); }
  .footer a { position: absolute; color: var(--white); font-size: 16px; text-decoration: underline; }
  .footer-contact { position: absolute; left: 663px; top: 35px; font-size: 18px; }
  .social { position: absolute; top: 29px; width: 36px; height: 36px; border-radius: 50%; background: var(--icon-bg); display: flex; align-items: center; justify-content: center; }
</style>
</head>
<body>
<div class="page">

  <header class="topbar">
    <nav class="topnav">
      <a href="#">Home</a><a href="#">Log In</a><a href="#">Contact Us</a>
    </nav>
    <div class="search">Search...
      <svg width="17" height="17" viewBox="0 0 17 17" aria-hidden="true"><circle cx="7" cy="7" r="5" fill="none" stroke="#fff" stroke-width="2"/><line x1="10.5" y1="10.5" x2="15" y2="15" stroke="#fff" stroke-width="2.4" stroke-linecap="round"/></svg>
    </div>
  </header>

  <div class="backdrop" role="img" aria-label="Soft-focus restaurant table with a plated meal and fork in the background"></div>

  <aside class="sidebar">
    <div class="brand"><span class="brand-dot"></span>Wheatless Table Co</div>
    <ul class="mainnav">
      <li>Shop</li>
      <li>Our Story</li>
      <li>Blog</li>
      <li>Hints &amp; Tips</li>
      <li class="active">Recipes</li>
      <li>Forums</li>
    </ul>
  </aside>
  <ul class="submenu">
    <li>Kids Pizza</li>
    <li>Gluten Free</li>
    <li>Kids Pizza</li>
    <li>Gluten Free</li>
  </ul>

  <section class="hero">
    <div class="hero-intro">
      <div class="hero-title">Wheatless<br>Table Co</div>
      <p class="hero-text">Lorem Ipsum has been the industry's standard dummy text ever since the 1500s.</p>
      <div class="btn-more">More Details.....</div>
    </div>
    <div class="hero-photo" role="img" aria-label="Platter of cold cuts, cheeses, dark bread, tomatoes and gherkins"></div>
  </section>

  <div class="picks-bar">daily picks
    <svg class="picks-arrow prev" viewBox="0 0 42 42" aria-hidden="true"><circle cx="21" cy="21" r="20" fill="#1a1a1a"/><polyline points="24,13 16,21 24,29" fill="none" stroke="#fff" stroke-width="3.5" stroke-linecap="round" stroke-linejoin="round"/></svg>
    <svg class="picks-arrow next" viewBox="0 0 42 42" aria-hidden="true"><circle cx="21" cy="21" r="20" fill="#1a1a1a"/><polyline points="18,13 26,21 18,29" fill="none" stroke="#fff" stroke-width="3.5" stroke-linecap="round" stroke-linejoin="round"/></svg>
  </div>

  <article class="pick" style="left:439px">
    <div class="pick-tab">WED</div>
    <div class="pick-body">
      <div class="pick-photo" role="img" aria-label="Slice of layered chocolate-banana dessert on a blue plate" style="background:radial-gradient(ellipse 35% 22% at 50% 48%,#4a2a1e 0%,rgba(74,42,30,0) 100%),radial-gradient(ellipse 30% 12% at 50% 62%,#f3efe8 0%,rgba(243,239,232,0) 100%),linear-gradient(180deg,#a6cf6c 0%,#cfdcb0 30%,#e2ddd4 50%,#8cbfd2 80%,#6fa9c0 100%)"></div>
      <div class="pick-stars">★★★★★<span>(21)</span></div>
      <div class="pick-name">chocolate-banana split dessert</div>
    </div>
  </article>

  <article class="pick" style="left:687px">
    <div class="pick-tab">TODAY</div>
    <div class="pick-body">
      <div class="pick-photo" role="img" aria-label="Grilled potato wedges with a small bowl of dipping sauce" style="background:radial-gradient(ellipse 40% 28% at 58% 48%,#b98436 0%,rgba(185,132,54,0) 100%),radial-gradient(ellipse 14% 10% at 18% 42%,#ffffff 0%,rgba(255,255,255,0) 100%),linear-gradient(180deg,#f2ebe4 0%,#ead7c6 55%,#f0c6b6 100%)"></div>
      <div class="pick-stars">★★★★★<span>(6)</span></div>
      <div class="pick-name">grilled steak fries with spicy blue cheese dipping</div>
    </div>
  </article>

  <article class="pick" style="left:929px">
    <div class="pick-tab">FRI</div>
    <div class="pick-body">
      <div class="pick-photo" role="img" aria-label="Row of glasses filled with red sangria" style="background:radial-gradient(ellipse 14% 22% at 18% 45%,#8c1e2a 0%,rgba(140,30,42,0) 100%),radial-gradient(ellipse 14% 22% at 50% 48%,#8c1e2a 0%,rgba(140,30,42,0) 100%),radial-gradient(ellipse 14% 22% at 82% 45%,#8c1e2a 0%,rgba(140,30,42,0) 100%),linear-gradient(180deg,#f6f4f2 0%,#ece6e2 60%,#d6d2ce 100%)"></div>
      <div class="pick-stars">★★★★★<span>(2)</span></div>
      <div class="pick-name">sangria party cups</div>
    </div>
  </article>

  <footer class="footer">
    <a href="#" style="left:204px;top:19px">Contact Us</a>
    <a href="#" style="left:204px;top:50px">FAQ's</a>
    <a href="#" style="left:384px;top:20px">Site Map</a>
    <a href="#" style="left:384px;top:51px">Privacy Policy</a>
    <div class="footer-contact">Contact:</div>
    <a class="social" href="#" style="left:754px" aria-label="Chat with us">
      <svg width="18" height="18" viewBox="0 0 18 18" aria-hidden="true"><path d="M2 3h14v9H8l-4 3v-3H2z" fill="#111"/></svg>
    </a>
    <a class="social" href="#" style="left:800px" aria-label="Share this page">
      <svg width="18" height="18" viewBox="0 0 18 18" aria-hidden="true"><line x1="5" y1="9" x2="13" y2="4" stroke="#111" stroke-width="2"/><line x1="5" y1="9" x2="13" y2="14" stroke="#111" stroke-width="2"/><circle cx="4.5" cy="9" r="2.6" fill="#111"/><circle cx="13.5" cy="4" r="2.6" fill="#111"/><circle cx="13.5" cy="14" r="2.6" fill="#111"/></svg>
    </a>
    <a class="social" href="#" style="left:845px" aria-label="Email updates">
      <svg width="18" height="18" viewBox="0 0 18 18" aria-hidden="true"><rect x="2" y="4" width="14" height="10" rx="1" fill="#111"/><polyline points="2.5,4.5 9,10 15.5,4.5" fill="none" stroke="#f2f2f2" stroke-width="1.5"/></svg>
    </a>
    <a class="social" href="#" style="left:891px" aria-label="Join the community">
      <svg width="18" height="18" viewBox="0 0 18 18" aria-hidden="true"><circle cx="9" cy="6" r="3.3" fill="#111"/><path d="M2.5 16c0-4 3-6 6.5-6s6.5 2 6.5 6z" fill="#111"/></svg>
    </a>
  </footer>

</div>
</body>
</html>
```